Business cards and logo for Delcourt Law, P.A.

I need a business card and logo design for a new law firm in Miami, Florida called Delcourt Law, P.A. I, Theodore K. Delcourt, am the only lawyer in the firm. The law firm will mainly serve businesses but will also handle many other cases. Preferred colors are green and/or gray, but open minded to other suggestions.

Industry/Entity Type

Legal

Contact Information for Business Card

Phone Number TBD. Address is:
41 NE 3RD AVE STE 200
MIAMI, FL 33142

```html
<!DOCTYPE html>
<html lang="en">
<head>
<meta charset="utf-8">
<title>Delcourt Law, P.A. — Business Card</title>
<link href="https://fonts.googleapis.com/css2?family=Tinos:wght@400;700&display=swap" rel="stylesheet">
<style>
  :root {
    --backdrop: #222222;
    --navy: #14466a;
    --gray: #a6a6a6;
    --muted: #9a9a9a;
    --paper: #ffffff;
  }
  * { margin: 0; padding: 0; box-sizing: border-box; }
  html, body {
    width: 1189px; height: 1200px; overflow: hidden;
    background: var(--backdrop);
    font-family: "Tinos", "Times New Roman", serif;
  }
  .card {
    position: absolute; left: 171px; width: 856px; height: 488px;
    border-radius: 22px; overflow: hidden;
  }
  .card--front { top: 67px; background: var(--navy); color: var(--paper); }
  .card--back { top: 626px; background: var(--paper); color: var(--navy); }

  .brand {
    position: absolute; transform: translateX(-50%);
    text-align: center; white-space: nowrap; font-weight: 700;
  }
  .brand__mark {
    display: flex; align-items: center; justify-content: center; gap: 12px;
    font-size: 34px; letter-spacing: 1px; height: 160px;
  }
  .brand__square { width: 18px; height: 18px; background: currentColor; }
  .brand__firm { font-size: 30px; line-height: 1.1; margin-top: 8px; }
  .brand__person { font-size: 26px; line-height: 1.2; }

  .card--front .brand { left: 428px; top: 130px; }
  .card--back .brand { left: 213px; top: 116px; }
  .card--back .brand__firm { font-size: 32px; }

  .divider {
    position: absolute; left: 416px; top: 100px; width: 1.5px; height: 253px;
    background: var(--gray);
  }
  .details { position: absolute; left: 470px; top: 98px; }
  .details__name { font-size: 30px; font-weight: 700; letter-spacing: 1.5px; line-height: 1.1; }
  .details__title { font-size: 22px; color: var(--muted); line-height: 1.1; }
  .details__address { margin-top: 78px; font-size: 23px; line-height: 1.3; letter-spacing: 0.3px; }
  .contact { margin-top: 16px; list-style: none; font-size: 23px; line-height: 1.28; }
  .contact__item { display: flex; align-items: center; gap: 8px; }
  .contact__icon { width: 24px; height: 24px; flex: none; }

  .accent-band { position: absolute; left: 0; bottom: 0; width: 100%; height: 25px; display: flex; }
  .accent-band__navy { width: 426px; background: var(--navy); }
  .accent-band__gray { flex: 1; background: var(--gray); }
</style>
</head>
<body>

<section class="card card--front" aria-label="Card front">
  <div class="brand">
    <div class="brand__mark"><span class="brand__square"></span>Delcourt Law</div>
    <div class="brand__firm">DELCOURT LAW, P.A.</div>
    <div class="brand__person">Theodore K. Delcourt</div>
  </div>
</section>

<section class="card card--back" aria-label="Card back">
  <div class="brand">
    <div class="brand__mark"><span class="brand__square"></span>Delcourt Law</div>
    <div class="brand__firm">DELCOURT LAW, P.A.</div>
    <div class="brand__person">Theodore K. Delcourt</div>
  </div>

  <div class="divider"></div>

  <div class="details">
    <div class="details__name">THEODORE K. DELCOURT</div>
    <div class="details__title">President</div>
    <div class="details__address">41 NE 3RD AVE STE 200<br>MIAMI, FL 33142</div>
    <ul class="contact">
      <li class="contact__item">
        <svg class="contact__icon" viewBox="0 0 24 24" aria-hidden="true">
          <rect width="24" height="24" rx="4" fill="var(--gray)"/>
          <path d="M8 5c-1.5 1-2 3-1 6s3.5 6 6 7.5c1.8 1 3 .5 4-.8l-2.6-2.4-1.6 1c-1.6-.8-3.3-2.8-4-4.6l1.2-1.4L8 5z" fill="#fff"/>
        </svg>
        <span>+01-555-010-0200</span>
      </li>
      <li class="contact__item">
        <svg class="contact__icon" viewBox="0 0 24 24" aria-hidden="true">
          <rect width="24" height="24" rx="4" fill="var(--gray)"/>
          <rect x="4" y="7" width="16" height="11" fill="none" stroke="#fff" stroke-width="1.5"/>
          <path d="M4 7l8 6 8-6M4 18l6-5M20 18l-6-5" fill="none" stroke="#fff" stroke-width="1.5"/>
        </svg>
        <span>info@delcourtlawpa.com</span>
      </li>
    </ul>
  </div>

  <div class="accent-band">
    <div class="accent-band__navy"></div>
    <div class="accent-band__gray"></div>
  </div>
</section>

</body>
</html>
```